Need a business card for my new home staging and redesign business. Business name: Larkspurrow Interiors. Subtitle: Styling and staging that helps homes sell

Target Market(s)

Realtors, home sellers

Industry/Entity Type

Real Estate

Contact Information for Business Card

I don't have a website address yet, or a business Facebook account, but would like to include those. Do not have a logo or any graphics

Font styles to use
Sans Serif

Colors

Designer to choose colors to be used in the design.

Requirements
Must have
• Placeholders for contact details, e.g. Phone, email, web address, etc.
Nice to have
• Sophisticated but somewhat whimsical feel. Perhaps a stylized star (or magic wand?) over the "I" in interiors to convey inspiration.
Should not have
• Nothing too cutesy, including cartoon wizards.

```html
<!DOCTYPE html>
<html lang="en">
<head>
<meta charset="utf-8">
<title>Larkspurrow Interiors – Business Card</title>
<link rel="stylesheet" href="https://fonts.googleapis.com/css2?family=Lato:wght@400;700&display=swap">
<style>
  :root{
    --bg:#2b2b2d;
    --ink:#0b0b0c;
    --paper:#f4f4f4;
    --red:#e8262e;
    --white:#ffffff;
    --grey-line:#cfcfcf;
    --grey-text:#9a9a9a;
    --grey-text-dark:#555555;
  }
  *{box-sizing:border-box;margin:0;padding:0}
  html,body{width:1200px;height:880px;overflow:hidden;background:var(--bg)}
  body{position:relative;font-family:"Lato",Arial,sans-serif}

  .card{position:absolute;width:600px;height:343px;border-radius:22px;overflow:hidden;
        box-shadow:0 14px 30px rgba(0,0,0,.45)}
  .card--back{left:60px;top:90px;background:var(--ink)}
  .card--front{left:540px;top:447px;background:var(--paper)}

  .brand{position:absolute;left:0;right:0;text-align:center}
  .brand__name{display:inline-flex;align-items:center;gap:12px;
               font-weight:400;font-size:44px;line-height:1}
  .brand__dot{width:10px;height:10px;border-radius:50%;background:var(--red);flex:none}
  .brand__tagline{font-size:15px;letter-spacing:.5px;margin-top:14px}

  .card--back .brand{top:110px;color:var(--white)}
  .card--back .brand__tagline{color:var(--grey-text)}
  .card--front .brand{top:62px;color:var(--ink)}
  .card--front .brand__tagline{color:var(--grey-text-dark)}

  .back__band{position:absolute;left:0;right:0;bottom:0;height:56px;background:var(--red);
              border-top:5px solid var(--white);display:flex;align-items:center;justify-content:center}
  .back__web{color:var(--white);font-size:15px;letter-spacing:2px}

  .front__dark{position:absolute;left:0;right:0;top:186px;height:104px;background:var(--ink);
               display:flex;align-items:center}
  .person{width:230px;text-align:right;padding-right:26px}
  .person__name{color:var(--white);font-size:24px;line-height:1}
  .person__role{color:var(--red);font-size:16px;margin-top:4px}
  .divider{width:1px;height:62px;background:var(--grey-line)}
  .contacts{list-style:none;padding-left:26px;color:var(--white);font-size:16px}
  .contacts li{display:flex;align-items:center;gap:10px;line-height:1.55}
  .contacts svg{width:15px;height:15px;flex:none}

  .front__band{position:absolute;left:0;right:0;bottom:0;height:53px;background:var(--red);
               border-top:4px solid var(--white);display:flex;align-items:center;justify-content:center}
  .front__address{color:var(--white);font-size:16px;letter-spacing:.3px}
</style>
</head>
<body>

  <section class="card card--back" aria-label="Card back">
    <div class="brand">
      <div class="brand__name"><span>Larkspurrow Interiors</span><span class="brand__dot"></span></div>
      <div class="brand__tagline">Styling and staging that helps homes sell</div>
    </div>
    <div class="back__band"><span class="back__web">www.larkspurrow.com</span></div>
  </section>

  <section class="card card--front" aria-label="Card front">
    <div class="brand">
      <div class="brand__name"><span>Larkspurrow Interiors</span><span class="brand__dot"></span></div>
      <div class="brand__tagline">Styling and staging that helps homes sell</div>
    </div>

    <div class="front__dark">
      <div class="person">
        <div class="person__name">Nora Vell</div>
        <div class="person__role">Founder</div>
      </div>
      <div class="divider"></div>
      <ul class="contacts">
        <li>
          <svg viewBox="0 0 16 16" aria-hidden="true"><rect x="4" y="1" width="8" height="14" rx="1.5" fill="none" stroke="var(--red)" stroke-width="1.6"/><circle cx="8" cy="12.5" r=".9" fill="var(--red)"/></svg>
          (555) 310-4827
        </li>
        <li>
          <svg viewBox="0 0 16 16" aria-hidden="true"><rect x="1" y="3" width="14" height="10" rx="1" fill="var(--red)"/><path d="M1.5 3.5 8 9l6.5-5.5" fill="none" stroke="var(--ink)" stroke-width="1.3"/></svg>
          hello@larkspurrow.com
        </li>
        <li>
          <svg viewBox="0 0 16 16" aria-hidden="true"><g fill="none" stroke="var(--red)" stroke-width="1.3"><circle cx="8" cy="8" r="6.5"/><ellipse cx="8" cy="8" rx="2.8" ry="6.5"/><path d="M1.5 8h13M2.5 4.8h11M2.5 11.2h11"/></g></svg>
          www.larkspurrow.com
        </li>
      </ul>
    </div>

    <div class="front__band"><span class="front__address">PO BOX 48 Fernhill Lane, 2nd street Ashbury</span></div>
  </section>

</body>
</html>
```